Dutch psychology podcast needs logo / art design

I need a logo / artwork for my new podcast on psychology/health called 'Het Heldere Kwartier'. In the podcast I talk to different experts on subjects as personal development, psychology, health, spirituality and entrepreneurship. I would like to see my brand colors back in the design (www.joramveldkuijl.nl) and my face in the artwork since I'm the host of the show.

My photo is included in the attachments and I've also added some examples of what I'm looking for.

Industry/Entity Type

Psychology

Colors

Designer to choose colors to be used in the design.

Requirements
Must have
• - Name of the show: 'Het Heldere Kwartier' (I prefer that this name is turned into a logo), see attachment of example of Harbor of Wonder
• - Subtitle: 'met Joram Veldkuijl' which is my name a the host
• - My picture, see attachments

```html
<!DOCTYPE html>
<html lang="nl">
<head>
<meta charset="utf-8">
<title>Het Heldere Kwartier – podcast artwork</title>
<link rel="stylesheet" href="https://fonts.googleapis.com/css2?family=Jost:wght@300;400;600;700&display=swap">
<style>
  :root {
    --page: #ffffff;
    --teal: #2fa79d;
    --teal-light: #5cc4bb;
    --teal-pale: #9fdcd5;
    --teal-deep: #2a8c84;
    --white: #ffffff;
    --band: #eef1f1;
    --ink-teal: #2b8f86;
  }
  * { margin: 0; padding: 0; box-sizing: border-box; }
  html, body { width: 1200px; height: 900px; overflow: hidden; background: var(--page); }
  body { position: relative; font-family: "Jost", "Futura", sans-serif; }

  .cover {
    position: absolute; left: 190px; top: 40px; width: 820px; height: 820px;
    background: var(--teal); overflow: hidden;
    box-shadow: 0 8px 24px rgba(0,0,0,.35);
  }
  .crowd-photo {
    position: absolute; inset: 0;
    background: linear-gradient(100deg, var(--teal-light) 0%, var(--teal) 45%, var(--teal-pale) 100%);
    opacity: .9;
  }
  .light-bar { position: absolute; top: 0; bottom: 0; background: rgba(255,255,255,.14); }
  .host-photo {
    position: absolute; left: 190px; top: 15px; width: 500px; height: 760px;
    border-radius: 150px 150px 20px 20px;
    background: linear-gradient(180deg, #c9a892 0%, #c09a84 38%, #1f2838 42%, #1b2333 100%);
  }
  .artwork { position: absolute; inset: 0; }

  .podcast-badge {
    position: absolute; left: 718px; top: 32px; width: 100px; height: 100px;
    background: var(--teal-deep); color: var(--white);
    display: flex; flex-direction: column; align-items: center; justify-content: flex-end;
    padding-bottom: 8px;
  }
  .podcast-badge svg { margin-bottom: 4px; }
  .podcast-badge span { font-weight: 600; font-size: 15px; letter-spacing: .5px; }

  .host-credit { position: absolute; left: 462px; top: 690px; color: var(--white); }
  .host-credit .met {
    position: absolute; left: 0; top: 8px; width: 158px; height: 40px;
    background: var(--white); color: var(--ink-teal);
    font-weight: 600; font-size: 34px; line-height: 40px; padding-left: 6px;
  }
  .host-credit .first {
    position: absolute; left: 168px; top: 0; font-weight: 700; font-size: 52px; line-height: 56px; white-space: nowrap;
  }
  .host-credit .last {
    position: absolute; left: 2px; top: 50px; font-weight: 300; font-size: 52px; line-height: 56px;
    letter-spacing: .5px; white-space: nowrap;
  }
</style>
</head>
<body>
  <section class="cover">
    <div class="crowd-photo" role="img" aria-label="Blurred group of smiling people in teal tint"></div>
    <div class="light-bar" style="left:75px;width:90px"></div>
    <div class="light-bar" style="left:230px;width:60px;top:140px"></div>
    <div class="light-bar" style="left:560px;width:65px;top:140px"></div>
    <div class="light-bar" style="left:755px;width:65px"></div>

    <div class="host-photo" role="img" aria-label="Portrait of the host, smiling, arms crossed, navy sweater"></div>

    <svg class="artwork" width="820" height="820" viewBox="0 0 820 820">
      <polygon points="0,785 820,580 820,820 0,820" fill="var(--teal-deep)"/>
      <g transform="translate(10,555) rotate(-13.5)">
        <text x="40" y="-70" fill="var(--white)" font-family="Jost, sans-serif" font-weight="700" font-size="108" textLength="210" lengthAdjust="spacingAndGlyphs">HET</text>
        <rect x="-60" y="-55" width="710" height="108" fill="var(--band)"/>
        <text x="30" y="37" fill="var(--ink-teal)" font-family="Jost, sans-serif" font-weight="700" font-size="108" textLength="570" lengthAdjust="spacingAndGlyphs">HELDERE</text>
        <rect x="110" y="62" width="440" height="108" fill="var(--band)"/>
        <text x="122" y="152" fill="var(--ink-teal)" font-family="Jost, sans-serif" font-weight="700" font-size="100" textLength="416" lengthAdjust="spacingAndGlyphs">KWARTIER</text>
        <polygon points="110,170 200,170 245,250" fill="var(--band)"/>
      </g>
    </svg>

    <div class="podcast-badge">
      <svg width="44" height="56" viewBox="0 0 44 56" fill="none" stroke="#fff" stroke-width="3" stroke-linecap="round">
        <rect x="12" y="3" width="20" height="30" rx="10" fill="#fff"/>
        <line x1="15" y1="14" x2="29" y2="14" stroke="var(--teal-deep)" stroke-width="2"/>
        <line x1="15" y1="20" x2="29" y2="20" stroke="var(--teal-deep)" stroke-width="2"/>
        <path d="M5 22 a17 17 0 0 0 34 0"/>
        <line x1="22" y1="39" x2="22" y2="49"/>
        <line x1="13" y1="51" x2="31" y2="51"/>
      </svg>
      <span>PODCAST</span>
    </div>

    <div class="host-credit">
      <div class="met">met</div>
      <div class="first">JORAM</div>
      <div class="last">VELDKUIJL</div>
    </div>
  </section>
</body>
</html>
```